Bioidentical Hormone Replacement Therapy

I need a rectangular brochure- sized flyer (one page) designed to hand out to patients that will capture their attention. The flyer will display our company name, logo, contact information, website and social media information provided below. We need people to know that we offer a personalized approach to medicine. The main purpose of the flyer is to convey the fact that we offer bioidentical hormone replacement therapy (BHRT) for women and men by a pellet insertion procedure even for non members. Symptoms this can help with are for Women:
Fatigue*
Trouble sleeping*
Irritability*
Anxiousness*
Mood swings*
Low mood*
Night sweats*
Hot flashes or flushes*
Weight gain*
Decreased sex drive*
Discomfort during intercourse*
Low bone density*
and for Men:
Low sex drive*
Increased body fat
(especially in the waist area)*
Loss of muscle mass and strength*
Reduced mental focus*
Feelings of anxiety*
Irritability*
Fatigue*
Elevated blood sugar*
High cholesterol*
Practice name: Brookhaven Internal Medicine
Address: 4382 Larkspur Lane, Columbia, SC. 20917
Phone: 803-671-5394
Email: jtrevor@brookhavenimd.example
Website: https://brookhavenimd.example
Facebook: https://www.facebook.com/profile.php?id=70938265147723
Updates
For sizing 3.5 inch or so by 8.5 inch or so inch is fine. Not sure what is standard printing paper size for flyer.
Target Market(s)
Medical Patients
Industry/Entity Type
Healthcare
Look and feel

```html
<!DOCTYPE html>
<html lang="en">
<head>
<meta charset="utf-8">
<title>Bioidentical Hormone Replacement Therapy – Brookhaven Internal Medicine</title>
<link href="https://fonts.googleapis.com/css2?family=Roboto:wght@300;400;700;900&display=swap" rel="stylesheet">
<style>
  :root {
    --brand-blue: #0057ae;
    --bullet-blue: #0a55b0;
    --ink: #111418;
    --ink-soft: #2a2f36;
    --panel-women: #e8f0f8;
    --panel-men: #cddff0;
    --white: #ffffff;
  }
  * { box-sizing: border-box; margin: 0; padding: 0; }
  html, body { width: 1200px; height: 848px; overflow: hidden; background: var(--white); }
  body { font-family: "Roboto", Arial, sans-serif; color: var(--ink); }

  .flyer { position: relative; width: 1200px; height: 848px; }

  .photo { position: absolute; top: 0; height: 318px; }
  .photo--women { left: 0; width: 600px;
    background: linear-gradient(160deg, #e9e3de 0%, #d9cfc9 40%, #e6b7c9 62%, #b9b4b3 100%); }
  .photo--men { left: 600px; width: 600px;
    background: linear-gradient(120deg, #f1f2f3 0%, #e4e7ea 45%, #8a929c 70%, #5d6670 100%); }

  .symptoms { position: absolute; top: 318px; height: 313px; }
  .symptoms--women { left: 0; width: 600px; background: var(--panel-women); }
  .symptoms--men { left: 600px; width: 600px; background: var(--panel-men); }

  .symptoms__title {
    position: absolute; top: 30px; font-size: 21.5px; font-weight: 900;
    letter-spacing: 0.6px; text-transform: uppercase; color: var(--ink);
  }
  .symptoms--women .symptoms__title { left: 31px; }
  .symptoms--men .symptoms__title { left: 37px; }

  .symptom-list { position: absolute; top: 76px; list-style: none; }
  .symptom-list li {
    position: relative; height: 36px; line-height: 36px; padding-left: 22px;
    font-size: 19px; font-weight: 300; color: var(--ink-soft); white-space: nowrap;
  }
  .symptom-list li::before {
    content: ""; position: absolute; left: 0; top: 13px; width: 11px; height: 11px;
    border-radius: 50%; background: var(--bullet-blue);
  }

  .symptoms--women .col-1 { left: 32px; }
  .symptoms--women .col-1 li { padding-left: 27px; }
  .symptoms--women .col-2 { left: 276px; }
  .symptoms--men .col-1 { left: 38px; }
  .symptoms--men .col-2 { left: 377px; }
  .symptoms--men .col-1 li { padding-left: 26px; }
  .symptoms--men .col-2 li { padding-left: 21px; }

  .banner {
    position: absolute; top: 631px; left: 0; width: 1200px; height: 49px;
    background: var(--brand-blue); color: var(--white);
    font-size: 30.3px; font-weight: 900; letter-spacing: 1.3px;
    text-align: center; line-height: 50px;
  }

  .contact-bar { position: absolute; top: 680px; left: 0; width: 1200px; height: 168px; }

  .brand-mark {
    position: absolute; left: 26px; top: 18px; width: 118px; height: 132px;
    display: flex; flex-direction: column; align-items: center; justify-content: center; gap: 8px;
  }
  .brand-mark__dot { width: 52px; height: 52px; border-radius: 50%; background: var(--brand-blue); }
  .brand-mark__name {
    font-size: 11px; font-weight: 700; color: var(--brand-blue);
    text-align: center; line-height: 1.2; letter-spacing: 0.5px; text-transform: uppercase;
  }

  .practice-name {
    position: absolute; left: 188px; top: 28px; font-size: 24px; font-weight: 900;
    letter-spacing: 0.6px; color: var(--brand-blue); text-transform: uppercase; white-space: nowrap;
  }

  .contact-line {
    position: absolute; display: flex; align-items: center; gap: 10px;
    font-size: 18.5px; font-weight: 400; color: var(--ink); white-space: nowrap;
  }
  .contact-line svg { flex: none; fill: var(--brand-blue); }
  .contact-line--address { left: 190px; top: 76px; }
  .contact-line--phone { left: 190px; top: 110px; }
  .contact-line--email { left: 649px; top: 29px; gap: 17px; }
  .contact-line--web { left: 649px; top: 72px; gap: 17px; }
  .contact-line--social { left: 649px; top: 114px; gap: 17px; }
</style>
</head>
<body>
<main class="flyer">
  <div class="photo photo--women" role="img" aria-label="Photo of a tired woman lying on a bed holding a hot water bottle"></div>
  <div class="photo photo--men" role="img" aria-label="Photo of a smiling man in a robe speaking with a doctor"></div>

  <section class="symptoms symptoms--women">
    <h2 class="symptoms__title">Symptoms for women</h2>
    <ul class="symptom-list col-1">
      <li>Fatigue*</li>
      <li>Trouble sleeping*</li>
      <li>Irritability*</li>
      <li>Anxiousness*</li>
      <li>Mood swings*</li>
      <li>Low mood*</li>
    </ul>
    <ul class="symptom-list col-2">
      <li>Night sweats*</li>
      <li>Hot flashes or flushes*</li>
      <li>Weight gain*</li>
      <li>Decreased sex drive*</li>
      <li>Discomfort during intercourse*</li>
      <li>Low bone density*</li>
    </ul>
  </section>

  <section class="symptoms symptoms--men">
    <h2 class="symptoms__title">Symptoms for men</h2>
    <ul class="symptom-list col-1">
      <li>Low sex drive*</li>
      <li>Increased body fat</li>
      <li>(especially in the waist area)*</li>
      <li>Loss of muscle mass and strength*</li>
      <li>Reduced mental focus*</li>
    </ul>
    <ul class="symptom-list col-2">
      <li>Feelings of anxiety*</li>
      <li>Irritability*</li>
      <li>Fatigue*</li>
      <li>Elevated blood sugar*</li>
      <li>High cholesterol*</li>
    </ul>
  </section>

  <h1 class="banner">BIOIDENTICAL HORMONE REPLACEMENT THERAPY</h1>

  <footer class="contact-bar">
    <div class="brand-mark">
      <span class="brand-mark__dot"></span>
      <span class="brand-mark__name">Brookhaven<br>Internal Medicine</span>
    </div>

    <div class="practice-name">Brookhaven Internal Medicine</div>

    <div class="contact-line contact-line--address">
      <svg width="16" height="20" viewBox="0 0 16 20"><path d="M8 0C3.6 0 0 3.5 0 7.9 0 13.6 8 20 8 20s8-6.4 8-12.1C16 3.5 12.4 0 8 0zm0 11a3.2 3.2 0 1 1 0-6.4A3.2 3.2 0 0 1 8 11z"/></svg>
      <span>4382 Larkspur Lane, Columbia, SC. 20917</span>
    </div>
    <div class="contact-line contact-line--phone">
      <svg width="18" height="18" viewBox="0 0 24 24"><path d="M6.6 10.8a15.1 15.1 0 0 0 6.6 6.6l2.2-2.2c.3-.3.7-.4 1-.2 1.1.4 2.3.6 3.6.6.6 0 1 .4 1 1V20c0 .6-.4 1-1 1A17 17 0 0 1 3 4c0-.6.4-1 1-1h3.5c.6 0 1 .4 1 1 0 1.3.2 2.5.6 3.6.1.3 0 .7-.2 1z"/></svg>
      <span>803-671-5394</span>
    </div>

    <div class="contact-line contact-line--email">
      <svg width="17" height="13" viewBox="0 0 17 13"><path d="M0 0h17v13H0zM1.5 1.5v.3l7 5 7-5v-.3zm0 2.2v7.8h14V3.7l-7 5z"/></svg>
      <span>jtrevor@brookhavenimd.example</span>
    </div>
    <div class="contact-line contact-line--web">
      <svg width="17" height="17" viewBox="0 0 24 24"><path d="M12 1a11 11 0 1 0 0 22 11 11 0 0 0 0-22zm7.9 10h-3.5a17 17 0 0 0-1.4-6.9A9 9 0 0 1 19.9 11zM12 3.1c1 1.2 2.2 4 2.4 7.9H9.6c.2-3.9 1.4-6.7 2.4-7.9zM9 4.1A17 17 0 0 0 7.6 11H4.1A9 9 0 0 1 9 4.1zM4.1 13h3.5A17 17 0 0 0 9 19.9 9 9 0 0 1 4.1 13zm7.9 7.9c-1-1.2-2.2-4-2.4-7.9h4.8c-.2 3.9-1.4 6.7-2.4 7.9zm3-1A17 17 0 0 0 16.4 13h3.5a9 9 0 0 1-4.9 6.9z"/></svg>
      <span>www.brookhavenimd.example</span>
    </div>
    <div class="contact-line contact-line--social">
      <svg width="17" height="17" viewBox="0 0 17 17"><circle cx="8.5" cy="8.5" r="7"/></svg>
      <span>www.socialpage.example/profile.php?id=70938265147723</span>
    </div>
  </footer>
</main>
</body>
</html>
```